Signage for a store*

logo on the two sides of the sign
in the middle is the name of the store witch is KORVELO
at the bottom of the two logos, one side for location/address and the other side is contact details phone number is 718-392-6170 address is 7342 THE SIGN WILL BEE 15 FEET BY 4 FEET I WOULD LIKE THAT THE
BACKGROUND OF THE SIGN SHOULD HAVE A NICE COLOR BASE
THAT GOES FOR A WINE STORE

```html
<!DOCTYPE html>
<html lang="en">
<head>
<meta charset="utf-8">
<title>KORVELO Store Sign</title>
<link href="https://fonts.googleapis.com/css2?family=Rubik:ital,wght@0,700;1,700&display=swap" rel="stylesheet">
<style>
  :root {
    --wine: #8b2a44;
    --wine-soft: #c9859a;
    --paper: #ffffff;
    --frame: #b5b5b5;
  }
  html, body {
    margin: 0;
    padding: 0;
    width: 1200px;
    height: 1200px;
    overflow: hidden;
    background: var(--paper);
  }
  .canvas {
    position: relative;
    width: 1198px;
    height: 1198px;
    border: 1px solid var(--frame);
    background: var(--paper);
  }
  .sign-band {
    position: absolute;
    left: 31px;
    width: 1139px;
    height: 304px;
  }
  .sign-band--phone { top: 286px; }
  .sign-band--address { top: 610px; }
  .band-shape {
    position: absolute;
    inset: 0;
    display: block;
  }
  .wine-glass-art {
    position: absolute;
    left: 45px;
    top: 8px;
    width: 96px;
    height: 282px;
    border-radius: 48px 48px 6px 6px;
    background: linear-gradient(180deg, var(--wine-soft) 0%, var(--wine) 100%);
  }
  .brand-mark {
    position: absolute;
    left: 173px;
    top: 122px;
    width: 200px;
    text-align: center;
    font-family: "Rubik", sans-serif;
    font-weight: 700;
    font-style: normal;
    font-size: 38px;
    line-height: 60px;
    color: var(--wine);
    letter-spacing: 1px;
  }
  .sign-text {
    position: absolute;
    left: 500px;
    margin: 0;
    font-family: "Rubik", sans-serif;
    font-weight: 700;
    font-style: italic;
    color: var(--paper);
  }
  .sign-text--phone {
    top: 108px;
    font-size: 68px;
    line-height: 80px;
    letter-spacing: 1px;
  }
  .sign-text--address {
    top: 54px;
    font-size: 58px;
    line-height: 68px;
    white-space: pre;
  }
</style>
</head>
<body>
<main class="canvas">

  <section class="sign-band sign-band--phone">
    <svg class="band-shape" width="1139" height="304" viewBox="0 0 1139 304" aria-hidden="true">
      <rect width="1139" height="304" fill="var(--wine)"/>
      <path d="M0 7 H325 C375 7 399 80 399 152 C399 224 375 297 325 297 H0 Z" fill="var(--paper)"/>
    </svg>
    <div class="wine-glass-art" role="img" aria-label="Illustration of wine dripping into a splashing wine glass"></div>
    <div class="brand-mark">KORVELO</div>
    <p class="sign-text sign-text--phone">718-392-6170</p>
  </section>

  <section class="sign-band sign-band--address">
    <svg class="band-shape" width="1139" height="304" viewBox="0 0 1139 304" aria-hidden="true">
      <rect width="1139" height="304" fill="var(--wine)"/>
      <path d="M0 7 H325 C375 7 399 80 399 152 C399 224 375 297 325 297 H0 Z" fill="var(--paper)"/>
    </svg>
    <div class="wine-glass-art" role="img" aria-label="Illustration of wine dripping into a splashing wine glass"></div>
    <div class="brand-mark">KORVELO</div>
    <p class="sign-text sign-text--address">3860  64th St
Brookvale, N.Y.
11862</p>
  </section>

</main>
</body>
</html>
```